Business Card Design for Kidvale (Hires out childrens play areas)

Looking to have a business card designed for a company we just bought. The company rents out childrens play areas.

I have uploaded a couple of examples of the kind of business card style I like. Here are two more examples:

https://quorvastudio.nz/project/bright-romp-branding/
https://imgvaultcdn.com/design_img/8841052/302917/302917_5518203_8841052_b73e19a2_image.jpg

I think a white card will be best due to all the colours in the logo.

Size we require: 3.75" x 2.25" (horizontally orientated) with a 0.125" bleed

Uploaded is two versions of our logo.

Details for the card:
1. My name: Liam Verster
2. Title: Managing Director
3. Phone no: 021 563 417
4. Email: liam@kidvale.co.nz
5. URL: www.kidvale.co.nz
6. Address:
PO Box 318625
Fernlea, Auckland

Let me know if you need anything else.

Target Market(s)

Hospitals, doctors surgeries, bed shops, etc.

Contact Information for Business Card

Details for the card:
1. My name: Liam Verster
3. Phone no: 021 563 417
5. URL: www.kidvale.co.nz
6. Address:
PO Box 318625
Fernlea, Auckland

Requirements
Should not have
• Not too busy.

```html
<!DOCTYPE html>
<html lang="en">
<head>
<meta charset="utf-8">
<title>Kidvale — Business Card</title>
<link rel="stylesheet" href="https://fonts.googleapis.com/css2?family=Chewy&family=Open+Sans:wght@300&display=swap">
<style>
  :root {
    --card-bg: #ffffff;
    --ink-deep: #0b5aa6;
    --ink-light: #2ab3e6;
    --brand-blue: #1466b8;
    --kid-purple: #a02fa8;
    --kid-teal: #1ea3cc;
    --kid-orange: #e98a23;
  }
  html, body {
    margin: 0;
    padding: 0;
    width: 1200px;
    height: 720px;
    overflow: hidden;
    background: var(--card-bg);
  }
  .card {
    position: relative;
    width: 1200px;
    height: 720px;
    background: var(--card-bg);
    font-family: "Open Sans", "Segoe UI", sans-serif;
    font-weight: 300;
    color: var(--ink-light);
  }
  .brand {
    position: absolute;
    left: 65px;
    top: 40px;
    width: 370px;
    height: 308px;
    display: flex;
    flex-direction: column;
    align-items: center;
    justify-content: center;
    gap: 10px;
  }
  .brand-mark {
    width: 118px;
    height: 118px;
    border-radius: 50%;
    background: var(--brand-blue);
    flex: none;
  }
  .brand-name {
    font-family: "Chewy", "Segoe UI", sans-serif;
    font-weight: 400;
    font-size: 116px;
    line-height: 1;
    color: var(--brand-blue);
  }
  .contact {
    position: absolute;
    left: 616px;
    top: 60px;
  }
  .person-name {
    margin: 0;
    font-family: "Chewy", "Segoe UI", sans-serif;
    font-weight: 400;
    font-size: 52px;
    line-height: 1;
    color: var(--ink-deep);
  }
  .person-title {
    margin: -6px 0 0;
    font-size: 24px;
    line-height: 1.1;
  }
  .address {
    margin: 44px 0 0;
    font-style: normal;
    font-size: 24px;
    line-height: 0.92;
  }
  .channels {
    list-style: none;
    margin: 40px 0 0;
    padding: 0;
  }
  .channel {
    display: flex;
    align-items: center;
    gap: 4px;
    height: 36px;
    margin-bottom: 20px;
    font-size: 24px;
  }
  .channel-icon {
    width: 34px;
    height: 34px;
    flex: none;
    fill: var(--ink-deep);
  }
  .channel-icon--globe {
    fill: none;
    stroke: var(--ink-deep);
    stroke-width: 2;
  }
  .kids-illustration {
    position: absolute;
    left: 618px;
    top: 480px;
    width: 478px;
    height: 200px;
    border-radius: 100px;
    background: linear-gradient(90deg, var(--kid-purple) 0%, var(--kid-teal) 50%, var(--kid-orange) 100%);
    box-shadow: 0 14px 18px rgba(0, 0, 0, 0.18);
  }
</style>
</head>
<body>
<div class="card">
  <div class="brand">
    <span class="brand-mark"></span>
    <span class="brand-name">Kidvale</span>
  </div>

  <div class="contact">
    <h1 class="person-name">Liam Verster</h1>
    <p class="person-title">Managing Director</p>

    <address class="address">
      PO Box 318625<br>
      Fernlea, Auckland
    </address>

    <ul class="channels">
      <li class="channel">
        <svg class="channel-icon" viewBox="0 0 34 34" aria-hidden="true">
          <path d="M3 12c0-5 7-7 14-7s14 2 14 7v3h-7v-3c-2-1-12-1-14 0v3H3z"/>
          <path d="M8 16h18l3 11H5z M14 20a3 3 0 1 0 6 0a3 3 0 1 0-6 0z" fill-rule="evenodd"/>
        </svg>
        <span>021 563 417</span>
      </li>
      <li class="channel">
        <svg class="channel-icon" viewBox="0 0 34 34" aria-hidden="true">
          <path d="M1 6h32v22H1z M4 8l13 11 13-11z" fill-rule="evenodd"/>
        </svg>
        <span>liam@kidvale.co.nz</span>
      </li>
      <li class="channel">
        <svg class="channel-icon channel-icon--globe" viewBox="0 0 34 34" aria-hidden="true">
          <circle cx="17" cy="17" r="14"/>
          <ellipse cx="17" cy="17" rx="6" ry="14"/>
          <path d="M3 17h28M5 10h24M5 24h24M17 3v28"/>
        </svg>
        <span>www.kidvale.co.nz</span>
      </li>
    </ul>
  </div>

  <div class="kids-illustration" role="img" aria-label="Illustration of three smiling cartoon children's heads in purple, blue and orange"></div>
</div>
</body>
</html>
```